Business Cards

Need a neat design for a new business card

Industry/Entity Type

Residential Construction

Contact Information for Business Card

Company Name- KOVE Construction Inc.
Owner- Marcus Tolliver
Phone number- (555)203-7481
Email- kovecohomes@brindlemail.example
SocialPage- www.socialpage.example/kovecohomes

Colors
fefdec

```html
<!DOCTYPE html>
<html lang="en">
<head>
<meta charset="utf-8">
<title>KOVE Construction – Business Cards</title>
<link href="https://fonts.googleapis.com/css2?family=Montserrat:wght@400;600;700&display=swap" rel="stylesheet">
<style>
  :root {
    --backdrop: #e4e4e4;
    --card-dark: #1a1a1a;
    --cream: #fefdec;
    --card-light: #f8f8f8;
    --ink: #141414;
    --ink-soft: #3a3a3a;
  }
  * { margin: 0; padding: 0; box-sizing: border-box; }
  html, body {
    width: 1200px; height: 960px; overflow: hidden;
    background: var(--backdrop);
    font-family: "Montserrat", sans-serif;
  }
  .sheet {
    position: relative; width: 1200px; height: 960px;
    display: flex; flex-direction: column; align-items: center; justify-content: center; gap: 44px;
  }
  .card {
    width: 700px; height: 400px; position: relative;
    box-shadow: 0 6px 18px rgba(0,0,0,.12);
  }
  .card-front {
    background: var(--card-dark);
    display: flex; align-items: center; justify-content: center;
  }
  .front-brand {
    display: flex; align-items: center; gap: 18px;
    color: var(--cream);
    font-weight: 600; font-size: 40px; letter-spacing: 4px;
  }
  .brand-square {
    width: 28px; height: 28px; background: var(--cream);
  }
  .card-back {
    background: var(--card-light);
    display: flex; align-items: center; padding: 0 56px;
  }
  .back-brand {
    display: flex; align-items: center; gap: 12px;
    color: var(--ink); font-weight: 600; font-size: 22px; letter-spacing: 2px;
    width: 280px;
  }
  .back-brand .brand-square { background: var(--ink); width: 18px; height: 18px; }
  .divider {
    width: 1.5px; height: 150px; background: var(--ink); margin: 0 28px 0 6px;
  }
  .contact { color: var(--ink); }
  .contact-name { font-weight: 700; font-size: 26px; line-height: 1.1; }
  .contact-role { font-weight: 400; font-size: 14px; color: var(--ink-soft); margin: 4px 0 16px; }
  .contact-list { list-style: none; font-size: 13.5px; line-height: 1.9; }
  .contact-list li { display: flex; align-items: center; gap: 8px; white-space: nowrap; }
  .contact-list svg { width: 13px; height: 13px; flex: none; fill: var(--ink); }
</style>
</head>
<body>
<main class="sheet">
  <section class="card card-front">
    <div class="front-brand">
      <span class="brand-square"></span>
      <span class="brand-name">KOVE Construction</span>
    </div>
  </section>

  <section class="card card-back">
    <div class="back-brand">
      <span class="brand-square"></span>
      <span class="brand-name">KOVE Construction</span>
    </div>
    <div class="divider"></div>
    <div class="contact">
      <p class="contact-name">Marcus Tolliver</p>
      <p class="contact-role">Owner</p>
      <ul class="contact-list">
        <li>
          <svg viewBox="0 0 24 24"><path d="M6.6 10.8a15.1 15.1 0 0 0 6.6 6.6l2.2-2.2c.3-.3.7-.4 1-.2 1.1.4 2.3.6 3.6.6.6 0 1 .4 1 1V20c0 .6-.4 1-1 1A17 17 0 0 1 3 4c0-.6.4-1 1-1h3.5c.6 0 1 .4 1 1 0 1.3.2 2.5.6 3.6.1.3 0 .7-.2 1z"/></svg>
          (555)203-7481
        </li>
        <li>
          <svg viewBox="0 0 24 24"><path d="M2 5h20v14H2z" fill="none"/><path d="M2 5h20v2l-10 6L2 7zM2 9l10 6 10-6v10H2z"/></svg>
          kovecohomes@brindlemail.example
        </li>
        <li>
          <svg viewBox="0 0 24 24"><rect x="3" y="3" width="18" height="18" rx="2"/></svg>
          www.socialpage.example/kovecohomes
        </li>
      </ul>
    </div>
  </section>
</main>
</body>
</html>
```